New graphics package for website

We're currently about to launch a product to insurance agents and we need to upgrade the graphics package for tundlex.io
The current site is http://tundlex.io
We'd like to upgrade the graphics package for this site - very simple. The site needs to have a very modern and elegant feel.
The site content should remain, we may add some. You can use lorem ipsum you need content to fill a space.
We need to add 3 page links - Home, Enroll, Request invitation
We also have an invitation page that needs to be upgraded (shall not be accessible from main site), the current page for that is: http://www.tundlex.io/webinar.php - content on this page cannot change, just needs a graphics over lay.
Final source files shall be AI or PSD and include all fonts and high-res images included.
Target Market(s)
Business to business - insurance agencies across the US are the only users of this site.
Industry/Entity Type
Insurance
Number of Pages Required
2 page
Requirements
Must have
- Multiple forms only in the inner pages:
- Enroll form for the enroll page.
- Invite form for the invite page
- Invite form shall only have name, email, phone, carrier

```html
<!DOCTYPE html>
<html lang="en">
<head>
<meta charset="utf-8">
<title>Tundlex.io — Insurance Agent Platform</title>
<link rel="stylesheet" href="https://fonts.googleapis.com/css2?family=Raleway:wght@300;400;500;600;700&family=Open+Sans:wght@400;600&display=swap">
<style>
:root{
  --orange:#f26a1b;
  --ink:#2d2d2d;
  --text:#6b6b6b;
  --muted:#9a9a9a;
  --line:#e2e2e2;
  --white:#ffffff;
  --dark:#262626;
  --darker:#1c1c1c;
}
*{box-sizing:border-box;margin:0;padding:0}
html,body{width:826px;height:1200px;overflow:hidden;background:var(--white)}
body{font-family:"Open Sans",Arial,sans-serif;color:var(--text);font-size:9px;line-height:1.5}
h1,h2,h3,h4,.nav,.logo{font-family:"Raleway",Helvetica,sans-serif}
.page{position:relative;width:826px;height:1200px}

/* header */
.site-header{height:33px;display:flex;align-items:center;justify-content:space-between;padding:0 62px 0 40px;background:var(--white);border-bottom:1px solid var(--line)}
.logo{display:flex;align-items:center;gap:6px;font-size:16px;font-weight:600;color:var(--orange)}
.logo-dot{width:12px;height:12px;border-radius:50%;background:var(--orange)}
.nav{display:flex;gap:4px;font-size:7.5px;font-weight:600;letter-spacing:.4px}
.nav a{color:var(--ink);text-decoration:none;padding:5px 10px}
.nav a.active{background:var(--orange);color:var(--white)}

/* hero */
.hero{position:relative;height:229px;background:linear-gradient(100deg,#5b6470 0%,#8a939c 35%,#b9c0c6 60%,#8e99a2 100%)}
.hero-photo{position:absolute;left:0;top:0;width:430px;height:229px;background:radial-gradient(ellipse at 45% 55%,#d8dadc 0%,#7d858c 55%,#4a5159 100%)}
.hero-copy{position:absolute;left:475px;top:86px;width:320px;color:var(--white)}
.hero-copy h2{font-size:14px;font-weight:400;letter-spacing:.5px}
.hero-copy h1{font-size:20px;font-weight:500;letter-spacing:.4px;margin-top:1px}
.hero-copy p{font-size:8px;margin-top:6px;opacity:.9}
.btn-outline{display:inline-block;margin-top:12px;border:1px solid var(--white);color:var(--white);font-size:7px;letter-spacing:1px;padding:5px 14px}

/* welcome */
.welcome{position:relative;height:268px;padding:20px 40px 0}
.welcome-main{width:570px}
.welcome h3{font-size:15px;font-weight:500;color:var(--ink)}
.sub{font-size:7.5px;color:var(--muted)}
.welcome-main>p{margin-top:10px;font-size:7.5px}
.media-row{display:flex;gap:14px;margin-top:12px}
.video-thumb{position:relative;width:128px;height:110px;flex:none;background:linear-gradient(135deg,#6d5a4b,#b89c84 50%,#48505a)}
.video-thumb svg{position:absolute;left:50%;top:50%;transform:translate(-50%,-50%)}
.media-text p{font-size:7.5px}
.media-text p+p{margin-top:10px}
.enroll-card{position:absolute;right:23px;top:20px;width:148px;border:1px solid var(--line);background:var(--white);padding:12px 10px 16px}
.enroll-card h4{font-size:8.5px;font-weight:600;color:var(--ink);margin-bottom:10px}
.field{height:17px;border:1px solid var(--line);margin-bottom:8px;font-size:7px;color:var(--muted);padding:2px 6px;display:flex;align-items:center;justify-content:space-between}
.btn-orange{display:block;background:var(--orange);color:var(--white);text-align:center;font-size:7.5px;font-weight:600;letter-spacing:.8px;padding:4px 0;margin-top:8px}

/* services */
.services{height:249px;padding:10px 40px 0;background:var(--white)}
.section-title{font-size:15px;font-weight:500;color:var(--ink)}
.cards{display:flex;gap:20px;margin-top:12px}
.service{width:235px}
.service-img{height:64px}
.caption{background:var(--dark);color:var(--white);font-size:7.5px;padding:3px 8px;font-family:"Raleway",sans-serif;font-weight:600}
.service p{font-size:7.5px;margin-top:6px}
.more{color:var(--orange);font-size:7.5px;font-weight:600;margin-top:3px;display:block}

/* banner */
.banner{height:107px;background:linear-gradient(180deg,#3a3a3a,#262626);color:var(--white);text-align:center;padding-top:22px}
.banner h2{font-size:19px;font-weight:500;letter-spacing:1px}
.banner p{font-size:7.5px;color:#c9c9c9;width:520px;margin:5px auto 0}
.banner .btn-orange{display:inline-block;padding:5px 18px;margin-top:8px}

/* blog */
.blog{height:214px;padding:18px 40px 0}
.posts{display:flex;gap:24px;margin-top:10px}
.post{width:225px;display:flex;gap:8px;border:1px solid var(--line);padding:8px}
.post-side{width:52px;flex:none}
.date{background:var(--dark);color:var(--white);text-align:center;font-family:"Raleway",sans-serif;padding:4px 0}
.date b{display:block;font-size:15px;line-height:1}
.date span{font-size:7px}
.post-img{height:52px;margin-top:5px;background:linear-gradient(135deg,#6b737b,#c2c6ca)}
.post h4{font-size:9px;font-weight:600;color:var(--ink);line-height:1.3}
.post p{font-size:7px;margin-top:4px}
.post-meta{font-size:6.5px;color:var(--muted);margin-top:6px;display:flex;justify-content:space-between;align-items:center;gap:4px}
.post-meta .btn-orange{margin:0;padding:3px 8px;display:inline-block;font-size:6.5px;flex:none}

/* footer */
.site-footer{position:absolute;left:0;bottom:0;width:826px;height:100px;background:var(--darker);color:#a9a9a9;padding:20px 40px 0;display:flex;justify-content:space-between}
.footer-left p{font-size:7px;width:300px}
.badges{display:flex;gap:6px;margin-top:12px}
.badge{width:30px;height:30px;background:#3a3a3a;border-radius:3px}
.footer-nav{font-family:"Raleway",sans-serif;font-size:7px;display:flex;gap:14px;letter-spacing:.4px}
.footer-right{text-align:right}
.footer-right p{font-size:6.5px;margin-top:8px}
</style>
</head>
<body>
<div class="page">
  <header class="site-header">
    <div class="logo"><span class="logo-dot"></span>Tundlex.io</div>
    <nav class="nav">
      <a class="active">HOME</a><a>ENROLL</a><a>REQUEST INVITATION</a><a>CONTACT US</a>
    </nav>
  </header>

  <section class="hero">
    <div class="hero-photo" role="img" aria-label="Businessman holding a group of agent icons protected under his hands"></div>
    <div class="hero-copy">
      <h2>LOREM IPSUM DOLOR</h2>
      <h1>CONSEC TETUR ADIPISCIN</h1>
      <p>Sed ut perspiciatis unde omnis iste natus error sit voluptatem accusantium.</p>
      <span class="btn-outline">READ MORE</span>
    </div>
  </section>

  <section class="welcome">
    <div class="welcome-main">
      <h3>Welcome to our site!</h3>
      <div class="sub">Making insurance leads simple</div>
      <p>Lorem ipsum dolor sit amet, consectetur adipiscing elit. Integer nec odio praesent libero sed cursus ante dapibus diam. Sed nisi nulla quis sem at nibh elementum imperdiet duis sagittis ipsum praesent mauris.</p>
      <div class="media-row">
        <div class="video-thumb" role="img" aria-label="Video still of agents meeting around a desk">
          <svg width="22" height="22" viewBox="0 0 22 22"><circle cx="11" cy="11" r="11" fill="rgba(255,255,255,.85)"/><path d="M9 6.5v9l7-4.5z" fill="#2d2d2d"/></svg>
        </div>
        <div class="media-text">
          <p>Fusce nec tellus sed augue semper porta mauris massa vestibulum lacinia arcu eget nulla. Class aptent taciti sociosqu ad litora torquent per conubia nostra per inceptos himenaeos curabitur sodales ligula.</p>
          <p>Curabitur tortor pellentesque nibh aenean quam in scelerisque sem at dolor maecenas mattis sed convallis tristique sem proin ut ligula vel nunc egestas porttitor morbi lectus risus iaculis vel.</p>
        </div>
      </div>
    </div>
    <aside class="enroll-card">
      <h4>Enroll for Tundlex Webinar</h4>
      <div class="field">Name</div>
      <div class="field">Email</div>
      <div class="field">Phone</div>
      <div class="field">Carrier <svg width="6" height="4" viewBox="0 0 6 4"><path d="M0 0h6L3 4z" fill="#9a9a9a"/></svg></div>
      <span class="btn-orange">ENROLL</span>
    </aside>
  </section>

  <section class="services">
    <h3 class="section-title">Our Featured Services</h3>
    <div class="sub">Solutions built for agencies</div>
    <div class="cards">
      <div class="service">
        <div class="service-img" role="img" aria-label="Agent shaking hands with a client" style="background:linear-gradient(135deg,#7a6a55,#c9b79b)"></div>
        <div class="caption">Auto Insurance</div>
        <p>Nulla quis sem at nibh elementum imperdiet duis sagittis ipsum praesent mauris fusce nec tellus.</p>
        <span class="more">Read More</span>
      </div>
      <div class="service">
        <div class="service-img" role="img" aria-label="Businessman on the phone" style="background:linear-gradient(135deg,#3d4650,#9aa3ab)"></div>
        <div class="caption">Life Insurance</div>
        <p>Nulla quis sem at nibh elementum imperdiet duis sagittis ipsum praesent mauris fusce nec tellus.</p>
        <span class="more">Read More</span>
      </div>
      <div class="service">
        <div class="service-img" role="img" aria-label="Row of colourful figures holding hands" style="background:linear-gradient(90deg,#e9e4da,#d8c7a4 50%,#b7c5d6)"></div>
        <div class="caption">Group Benefits</div>
        <p>Nulla quis sem at nibh elementum imperdiet duis sagittis ipsum praesent mauris fusce nec tellus.</p>
        <span class="more">Read More</span>
      </div>
    </div>
  </section>

  <section class="banner" role="img" aria-label="Dark band over a faint city photo">
    <h2>DOMINATE YOUR LOCAL INSURANCE MARKETS</h2>
    <p>Curabitur sodales ligula in libero sed dignissim lacinia nunc curabitur tortor pellentesque nibh aenean quam in scelerisque sem at dolor maecenas mattis.</p>
    <span class="btn-orange">Get Started</span>
  </section>

  <section class="blog">
    <h3 class="section-title">Latest from blog</h3>
    <div class="sub">News and tips for agents</div>
    <div class="posts">
      <article class="post">
        <div class="post-side">
          <div class="date"><b>21</b><span>Dec</span></div>
          <div class="post-img" role="img" aria-label="Agents working at a desk"></div>
        </div>
        <div>
          <h4>Lorem ipsum dolor sit amet sit lor</h4>
          <p>Sed dignissim lacinia nunc curabitur tortor pellentesque nibh aenean quam.</p>
          <div class="post-meta">Posted by Mara Lindqvist <span class="btn-orange">Read More</span></div>
        </div>
      </article>
      <article class="post">
        <div class="post-side">
          <div class="date"><b>21</b><span>Dec</span></div>
          <div class="post-img" role="img" aria-label="Team meeting in an office"></div>
        </div>
        <div>
          <h4>Lorem ipsum dolor sit amet sit lor</h4>
          <p>Sed dignissim lacinia nunc curabitur tortor pellentesque nibh aenean quam.</p>
          <div class="post-meta">Posted by Mara Lindqvist <span class="btn-orange">Read More</span></div>
        </div>
      </article>
    </div>
  </section>

  <footer class="site-footer">
    <div class="footer-left">
      <p>Copyright © 2015 Tundlex. All rights reserved. Terms and privacy policy apply.</p>
      <div class="badges"><span class="badge"></span><span class="badge"></span></div>
    </div>
    <div class="footer-right">
      <div class="footer-nav"><span>HOME</span><span>ENROLL</span><span>REQUEST INVITATION</span><span>CONTACT US</span></div>
      <p>tundlex.io</p>
    </div>
  </footer>
</div>
</body>
</html>
```